Flyer-Design für nachhaltige Familienberatung
Reiche Ideenvielfalt (viele sehr verschiedene Designvorschläge), prompte Umsetzung aller Änderungsideen während und nach dem Wettbewerb und dazu ein sehr freundlicher Kontakt - so macht die Zusammenarbeit wirklich Spaß! Vielen Dank dafür!
Zielgruppe
Ich bin Kleinunternehmerin und berate junge Familien (auch Schwangere, Alleinerziehende und andere Angehörige) zu den Themen Stoffwindeln, Windelfrei, Babyschlaf und bedürfnis-/bindungsorientierter Erziehung. Außerdem biete ich Paarberatung und Einzelcoaching für Mütter und - gemeinsam mit meinem Mann - für Väter an.
Der Name 'Familie MiTi' steht für Mirja und Till, mich und meinem Mann, gleichzeitig ein Wortspiel mit einer 'Hasenfamilie', auf das gern angespielt werden kann.
Weitere Informationen zum Angebot können der Internetseite www.familie-miti.example entnommen werden.
Aufgabenstellung
Das Design sollte farblich und stilistisch zum Logo passen. Naturverbundenheit/Nachhaltigkeit und Familienleben/Geborgenheit dürfen im Mittelpunkt stehen.
Mein Angebot ist vielfältig - umso wichtiger ist eine übersichtliche klare Darstellung. Der Flyer sollte junge Familien ansprechen. Er sollte hochwertig und liebevoll wirken: die Leser*innen sollten ermutigt werden, mich einfach unverbindlich anzurufen/mir zu schreiben (E-Mail, Signal, WhatsApp, Facebook-Messenger) und mehr über das Angebot zu erfahren.
Die Flyer werden vor allem in Geburtshäusern, Krankenhäusern, Familienzentren und bei Frauen-/Kinderärzt*innen und Hebammen ausliegen. Außerdem werden sie durch Kooperationspartner*innen (Still-/Trageberaterinnen, in Geburtsvorbereitungskursen) verteilt.
Die hochgeladenen Fotos dürfen, müssen aber nicht verwendet werden.

```html
<!DOCTYPE html>
<html lang="de">
<head>
<meta charset="utf-8">
<title>Familie MiTi – Flyer</title>
<link href="https://fonts.googleapis.com/css2?family=Arimo:wght@400;700&family=Roboto+Condensed:wght@700&display=swap" rel="stylesheet">
<style>
  :root{
    --bg:#e4e4e4;
    --paper:#ffffff;
    --panel:#eef5bf;
    --band:#f6f9df;
    --olive:#7a8a1e;
    --orange:#f07a12;
    --text:#2f2f2f;
  }
  *{box-sizing:border-box;margin:0;padding:0}
  html,body{width:1200px;height:1200px;overflow:hidden;background:var(--bg)}
  body{position:relative;font-family:"Arimo",Arial,sans-serif;color:var(--text)}
  .page{position:absolute;top:217px;width:496px;height:722px;background:var(--paper);overflow:hidden}
  .page--front{left:84px}
  .page--back{left:619px;width:494px}
  .panel{position:absolute;left:17px;right:17px;top:18px;bottom:18px;background:var(--panel)}

  /* front */
  .header-band{position:absolute;left:17px;top:18px;width:300px;height:108px;background:linear-gradient(90deg,var(--band),var(--panel))}
  .tagline{position:absolute;left:20px;top:45px;width:280px;text-align:center;font-size:12.5px;line-height:17px;color:var(--olive)}
  .tagline strong{font-weight:700}
  .tagline .url{display:block;margin-top:6px;color:var(--orange);font-weight:700}
  .brand{position:absolute;left:262px;top:164px;display:flex;align-items:center;gap:8px;font-size:25px;line-height:30px;color:var(--orange);letter-spacing:1px;font-weight:400}
  .brand-dot{width:14px;height:14px;border-radius:50%;background:var(--olive)}
  .topic{position:absolute;height:20px;padding:0 5px;background:var(--olive);color:#fff;font-family:"Roboto Condensed",Arial,sans-serif;font-weight:700;font-size:11px;line-height:20px;white-space:nowrap}
  .connectors{position:absolute;left:0;top:0}
  .photo{position:absolute;border-radius:50%;border:5px solid var(--olive)}
  .photo--big{border-width:4px}
  .contact{position:absolute;right:21px;top:586px;text-align:right;font-size:12px;line-height:15.5px}
  .contact .name{font-weight:700}
  .contact .gap{height:12px}

  /* back */
  .back-photo{position:absolute;left:347px;top:0;width:148px;height:156px;border-radius:0 0 50% 50% / 0 0 50% 50%;border:2px solid var(--olive);border-top:none}
  .back-title{position:absolute;left:32px;top:36px;font-size:18px;font-weight:700;color:var(--olive);white-space:nowrap}
  .offer{position:absolute;left:37px;top:80px;width:420px;font-size:9.6px;line-height:13.6px;text-align:justify}
  .offer h3{font-size:9.6px;font-weight:700;text-decoration:underline;margin:0 0 14px}
  .offer p{margin-bottom:14px}
  .offer .narrow{display:block;padding-right:110px;text-align:left}
</style>
</head>
<body>

<section class="page page--front">
  <div class="panel"></div>
  <div class="header-band"></div>
  <p class="tagline"><strong>Beratung, Begleitung und Workshops</strong><br>für Mütter, Väter und Familien<br>im Landkreis Talheim und Umgebung<span class="url">www.familie-miti.example</span></p>

  <div class="brand"><span class="brand-dot"></span><span>FAMILIE MITI</span></div>

  <svg class="connectors" width="496" height="722" viewBox="0 0 496 722" fill="none" stroke="#7a8a1e" stroke-width="1.5">
    <polyline points="100,203 85,203 85,240"/>
    <polyline points="252,231 240,231 225,249"/>
    <polyline points="360,297 345,297 330,316"/>
    <polyline points="387,392 372,392 365,430"/>
  </svg>

  <div class="topic" style="left:100px;top:193px">Paar- und Einzelbegleitung</div>
  <div class="topic" style="left:252px;top:220px">Baby- und Kleinkindschlaf</div>
  <div class="topic" style="left:360px;top:287px">moderne Stoffwindeln</div>
  <div class="topic" style="left:387px;top:382px">(Teilzeit-)Windelfrei</div>

  <div class="photo" role="img" aria-label="Foto: Vater hält Kind im Park" style="left:59px;top:234px;width:88px;height:88px;background:radial-gradient(circle at 50% 40%,#8d8470,#4f5a32)"></div>
  <div class="photo" role="img" aria-label="Foto: schlafendes Kleinkind mit Teddybär" style="left:185px;top:249px;width:88px;height:88px;background:radial-gradient(circle at 50% 45%,#b89470,#4e5f86)"></div>
  <div class="photo" role="img" aria-label="Foto: Kleinkind in Stoffwindel auf der Wiese" style="left:291px;top:312px;width:90px;height:90px;background:radial-gradient(circle at 50% 50%,#c4a890,#5d8a3a)"></div>
  <div class="photo" role="img" aria-label="Foto: Kind sitzt auf dem Töpfchen" style="left:357px;top:427px;width:78px;height:78px;background:radial-gradient(circle at 50% 50%,#e6d0b8,#6f8aa8)"></div>
  <div class="photo photo--big" role="img" aria-label="Foto: schlafendes Neugeborenes mit Kuscheltier" style="left:-9px;top:364px;width:352px;height:352px;background:radial-gradient(circle at 45% 55%,#efd9c3,#d6bfa6 55%,#b9a48c)"></div>

  <div class="contact">
    <div class="name">Familie MiTi</div>
    <div>Mirja Welkert</div>
    <div>Lindenweg 12</div>
    <div>34567 Talheim</div>
    <div class="gap"></div>
    <div>Telefon: 0151-00000000</div>
    <div>E-Mail: mirja@familie-miti.example</div>
    <div>oder till@familie-miti.example</div>
  </div>
</section>

<section class="page page--back">
  <div class="panel"></div>
  <div class="back-photo" role="img" aria-label="Foto: Kleinkind krabbelt auf eine Ziege zu" style="background:linear-gradient(180deg,#6f9a45 0%,#7d9a55 55%,#8a8478 56%,#9a9488 100%)"></div>
  <h2 class="back-title">Wir bieten euch Beratung und Unterstützung...</h2>

  <div class="offer">
    <h3>… bei unruhigen Nächten mit eurem Baby</h3>
    <p><span class="narrow">Mit der Geburt eines Kindes ist es aus mit den ruhigen Nächten, hört man oft. Doch lange Nächte zehren an den Kräften der Eltern und nicht selten fühlen sie sich allein gelassen. Mit einer bindungs­orientierten Schlafberatung kann ein artgerechter Weg zu besserem</span>und erholsamerem Schlaf für Eltern und Kind(er) von etwa 0-2 Jahren gefunden werden.</p>

    <h3>… beim trocken bleiben oder werden</h3>
    <p>Schon Neugeborene haben ein angeborenes Bedürfnis nach Sauberkeit, dem Eltern ohne viel Aufwand entgegen kommen können. Oder es vielleicht erstmal ausprobieren und dann weitersehen. In einer Windelfrei / Nappy-Free-Beratung erfahrt ihr u.a., wie und wo Babys kindgerecht und entspannt ihr großes und kleines Geschäft machen können.</p>
    <p>Kinder, die mit dieser Methode aufgewachsen sind, sind oft schon mit weniger als einem Jahr trocken. Doch auch wenn euer Kind mit Windeln aufgewachsen ist und sich mit dem Trocken werden schwer tut, sind wir für euch da – und das ganz ohne zwanghaftes Toilettentraining.</p>

    <h3>… beim Wickeln mit modernen Stoffwindeln</h3>
    <p>Stoffwindeln sind gesünder, ökologischer und langfristig kostengünstiger als Wegwerfwindeln und dabei genauso leicht zu benutzen. Außerdem verlieren Babys und Kleinkinder, die mit Stoff gewickelt werden, nicht das Gefühl für ihre Ausscheidungen und werden so häufig (ohne nappy) bereits mit unter zwei Jahren trocken.</p>
    <p>Damit ihr aus dem scheinbar undurchdringlichen (Stoffwindel) Dschungel ins bunte Paradies findet, in dem es für jedes Kind und jede Betreuungsperson die passende, einfache, schöne Windel gibt, beraten wir euch gern. Ihr lernt die verschiedenen modernen Windelsysteme kennen, könnt die Materialien anfassen und die Anwendung an Stoffpuppen ausprobieren.</p>

    <h3>Begleitung und Beratung</h3>
    <p>Stillen, wickeln, tragen, schlafen, wickeln, spielen, stillen, wickeln… Der Alltag als junge Familie ist plötzlich ganz anders als bisher. Andere Dinge sind wichtig geworden und die ein oder andere Situation kann ganz schön überfordern. Da kommt so ein kleines Wunder zur Welt und plötzlich ist man Eltern. Das kann ein Ungleichgewicht in die Beziehung bringen. Eine Paarberatung kann euch helfen, wieder miteinander ins Gespräch zu kommen und einen gemeinsamen Weg als Liebespaar und Eltern zu finden.</p>
    <p>Auch als einzelne (werdende) Elternteile könnt ihr gern eine Beratung in Anspruch nehmen. Zum Beispiel, wenn ihr das Gefühl habt, von eurer neuen Rolle oder all den gut gemeinten Ratschlägen aus dem Umfeld überfordert zu sein oder einfach gar nicht mehr wisst, wo euch der Kopf steht. Wenn ihr für euch selbst gut sorgt, habt ihr mehr Energie, das Familienleben zu meistern, ja sogar zu genießen.</p>
  </div>
</section>

</body>
</html>
```